Creative way to lay out a career advancement graphic

Are you a designer with a knack for turning complex concepts into visually captivating masterpieces? We have an exciting project that needs your unique talent! We're on the lookout for a creative designer to help us visualize our company's diverse career paths. Our organization offers a plethora of opportunities in project management, engineering, sales, and more. We want to showcase these pathways in a visually engaging manner to empower potential job candidates with a clear understanding of their advancement options within our company. Design must be flexible and able to be edited.

Check out the attached examples of the positions we'd like to include in this visualization (doc "inside sales" are correct positions). Your task will be to transform this information into a visually stunning representation that's both informative and inspiring.
This project is not just about design—it's about shaping the narrative of career growth and opportunity within our organization. Your creative input will play a vital role in helping us attract top talent and communicate our company's commitment to fostering professional development. Brand guidelines are also attached for reference. The document titled "parvel" demonstrates a badly done version of what we are trying to achieve. We want to denote multiple routes of advancement. You don't have to get the paths completely correct, you just need to show how it could be approached in a design. For example, A "submittal Specialist" could become a "project manager" but also could ascend to the role of "Industrial Estimator" if they want to move in that direction.

```html
<!DOCTYPE html>
<html lang="en">
<head>
<meta charset="utf-8">
<title>Orvane Career Paths</title>
<link href="https://fonts.googleapis.com/css2?family=Poppins:wght@400;500;600;700;800&family=Oswald:wght@500&display=swap" rel="stylesheet">
<style>
  :root{
    --stage:#979591;
    --paper:#ffffff;
    --orange:#f8931d;
    --yellow:#fdc010;
    --ink:#111111;
    --navy:#13263a;
    --map:#f4f4f4;
  }
  *{box-sizing:border-box;margin:0;padding:0}
  html,body{width:1200px;height:799px;overflow:hidden;background:var(--stage)}
  .sheet{
    position:absolute;left:0;top:95px;width:1646px;height:834px;
    background:var(--paper);transform:scale(0.729);transform-origin:0 0;
    font-family:"Poppins",sans-serif;
  }
  .map-area{position:absolute;left:80px;top:60px;width:1400px;height:700px;
    background:radial-gradient(ellipse at center,var(--map) 0%,rgba(244,244,244,0.4) 60%,rgba(255,255,255,0) 80%);}
  .brand{position:absolute;left:41px;top:72px}
  .brand-name{display:flex;align-items:center;gap:14px;font-weight:800;font-size:62px;line-height:1;color:var(--ink);letter-spacing:1px}
  .brand-dot{width:52px;height:52px;border-radius:50%;background:var(--yellow)}
  .paths{position:absolute;left:0;top:0;width:1646px;height:834px;z-index:2;pointer-events:none}
  .card{position:absolute;width:187px;border-radius:10px;padding-top:53px;z-index:1}
  .card--orange{background:var(--orange);color:#fff}
  .card--yellow{background:var(--yellow);color:var(--ink)}
  .card--dark{color:var(--ink)}
  .avatar{position:absolute;left:50%;top:-38px;width:82px;height:82px;margin-left:-41px;
    border-radius:50%;border:6px solid var(--ink);background:var(--yellow);box-shadow:0 0 0 5px #fff}
  .card--yellow .avatar{background:var(--orange)}
  .avatar--grey{border-color:#8d8d8d}
  .role{margin:0 -8px;background:var(--ink);color:#fff;font-weight:700;font-size:14px;
    height:22px;line-height:22px;text-align:center;white-space:nowrap;letter-spacing:0.2px}
  .role--small{font-size:11.5px}
  .role--condensed{font-family:"Oswald",sans-serif;font-weight:500;font-size:13px}
  .duties{list-style:none;padding:5px 10px 8px 22px;font-size:10.6px;line-height:12.4px}
  .duties li{position:relative;margin-bottom:3px}
  .duties li::before{content:"";position:absolute;left:-13px;top:3px;width:7px;height:7px;border-radius:50%;background:var(--ink)}
  .card--yellow .duties li::before{background:#fff}
</style>
</head>
<body>
<div class="sheet">
  <div class="map-area" role="img" aria-label="Faint world map backdrop"></div>

  <div class="brand">
    <div class="brand-name"><span class="brand-dot"></span>ORVANE</div>
  </div>

  <svg class="paths" viewBox="0 0 1646 834" aria-hidden="true">
    <defs>
      <marker id="head" markerUnits="userSpaceOnUse" markerWidth="16" markerHeight="16" refX="8" refY="8" orient="auto">
        <path d="M0 0 L16 8 L0 16 Z" fill="#13263a"/>
      </marker>
      <marker id="head-lg" markerUnits="userSpaceOnUse" markerWidth="30" markerHeight="34" refX="10" refY="17" orient="auto">
        <path d="M0 0 L30 17 L0 34 Z" fill="#13263a"/>
      </marker>
    </defs>
    <g fill="none" stroke="#13263a" stroke-width="4" marker-end="url(#head)">
      <path d="M686 250 H610 Q594 250 594 266 V276"/>
      <path d="M794 314 V292"/>
      <path d="M794 537 V515"/>
      <path d="M1018 278 V300"/>
      <path d="M1018 543 V565"/>
      <path d="M920 712 H902"/>
      <path d="M250 456 H232"/>
      <path d="M475 456 H457"/>
      <path d="M1173 342 V258 Q1173 244 1159 244 H1150"/>
      <path d="M1173 542 V622 Q1173 634 1159 634 H1150"/>
      <path d="M1343 297 H1324 Q1310 297 1310 311 V322"/>
    </g>
    <path d="M1553 565 H1626 V366 H1574" fill="none" stroke="#13263a" stroke-width="12" marker-end="url(#head-lg)"/>
  </svg>

  <article class="card card--orange" style="left:33px;top:352px;height:180px">
    <span class="avatar" role="img" aria-label="Profile avatar"></span>
    <h2 class="role">VICE PRESIDENT, SALES</h2>
    <ul class="duties"><li>Sales strategy development</li><li>Revenue generation</li><li>Market analysis</li><li>Sales forecasting and budgeting</li><li>Team Leadership</li></ul>
  </article>
  <article class="card card--yellow" style="left:256px;top:352px;height:180px">
    <span class="avatar" role="img" aria-label="Profile avatar"></span>
    <h2 class="role">SALES LEADERSHIP</h2>
    <ul class="duties"><li>Sets sets goals and targets</li><li>Sales team supervision, mentoring, training and coaching</li><li>Sales strategy development and implementation</li></ul>
  </article>
  <article class="card card--orange" style="left:481px;top:352px;height:180px">
    <span class="avatar" role="img" aria-label="Profile avatar"></span>
    <h2 class="role">OUTSIDE SALES</h2>
    <ul class="duties"><li>Prospecting and lead generation</li><li>Building and maintaining relationships</li><li>Closing sales and achieving targets.</li></ul>
  </article>

  <article class="card card--orange" style="left:702px;top:82px;height:222px">
    <span class="avatar" role="img" aria-label="Profile avatar"></span>
    <h2 class="role">LEAD PROJECT MANAGER</h2>
    <ul class="duties"><li>Prospecting and lead generation</li><li>Building and maintaining relationships</li><li>Closing sales and achieving targets.</li></ul>
  </article>
  <article class="card card--orange card--dark" style="left:702px;top:352px;height:180px">
    <span class="avatar" role="img" aria-label="Profile avatar"></span>
    <h2 class="role">LEAD TECHNICAL ENGINEER</h2>
    <ul class="duties"><li>Team leadership, mentoring and training</li><li>Technical sales liaison</li><li>Influence specifications</li><li>Read &amp; interpret specifications</li></ul>
  </article>
  <article class="card card--orange" style="left:702px;top:575px;height:222px">
    <span class="avatar" role="img" aria-label="Profile avatar"></span>
    <h2 class="role">LEAD PROJECT ENGINEER</h2>
    <ul class="duties"><li>Team leadership, mentoring and training</li><li>Technical expertise + engineering support</li><li>Subject matter expert relating to job, equipment &amp; commissioning</li><li>Quality control and project execution</li><li>Continuous improvement</li></ul>
  </article>

  <article class="card card--yellow" style="left:924px;top:116px;height:181px">
    <span class="avatar" role="img" aria-label="Profile avatar"></span>
    <h2 class="role role--small">PROJECT MANAGER</h2>
    <ul class="duties"><li>Project planning and organization</li><li>Monitoring and control</li><li>Customer service and communication</li></ul>
  </article>
  <article class="card card--orange" style="left:924px;top:347px;height:203px">
    <span class="avatar" role="img" aria-label="Profile avatar"></span>
    <h2 class="role role--small">INDUSTRIAL ESTIMATOR (SENIOR)</h2>
    <ul class="duties"><li>Quote preparation for more complex jobs</li><li>Specification and drawing review</li><li>Customer and vendor relationship</li><li>Analyze competitive pricing</li><li>Support outside sales</li></ul>
  </article>
  <article class="card card--yellow" style="left:924px;top:609px;height:181px">
    <span class="avatar" role="img" aria-label="Profile avatar"></span>
    <h2 class="role role--small">PROJECT ENGINEER</h2>
    <ul class="duties"><li>Technical expertise + engineering Support</li><li>Subject matter expert relating to job, equipment and commissioning</li><li>Quality control and project execution</li></ul>
  </article>

  <article class="card card--yellow" style="left:1144px;top:352px;height:180px">
    <span class="avatar" role="img" aria-label="Profile avatar"></span>
    <h2 class="role role--small">INDUSTRIAL ESTIMATOR (JUNIOR)</h2>
    <ul class="duties"><li>Quote preparation for less complex jobs</li><li>Specification and drawing Review</li><li>Vendor relationship</li><li>Support outside sales</li></ul>
  </article>

  <article class="card card--orange" style="left:1363px;top:237px;height:181px">
    <span class="avatar avatar--grey" role="img" aria-label="Profile avatar"></span>
    <h2 class="role role--condensed">SUBMITTAL SPECIALIST</h2>
    <ul class="duties"><li>Document control and management</li><li>Submittal preparation and review</li><li>Communication and co-ordination</li></ul>
  </article>
  <article class="card card--yellow" style="left:1363px;top:470px;height:181px">
    <span class="avatar avatar--grey" role="img" aria-label="Profile avatar"></span>
    <h2 class="role role--condensed">PROJECT COORDINATOR (GATEKEEPER)</h2>
    <ul class="duties"><li>Data entry for projects</li><li>Reviews project complexity and assigns accordingly</li></ul>
  </article>
</div>
</body>
</html>
```